Brightwell is a company offering Colon Hydrotherapy (or colonics)

Brightwell offers Colon Hydrotherapy using an innovative FDA approved system from the USA. The system is called the TORVA system. The clinic is based in Whangarei, Northland and is the first business of this kind for Northland.
I used to use a design from the Prontaleaf website - a water symbol. However, I want a design that will convey freshness. I want something new and clean which conveys vitality and revitalisation .... perhaps water or bubbles but which brings across the idea of detoxing (which is what colon hydrotherapy does)
The clinic will only be completed in April so for now I have put my mobile number but once in the clinic this will need to be changed to a landline number ... the email address will also change. Thanks for any ideas you give me,
Updates

Hi. I need the name Brightwell first and foremost as this is the name of the Company Underneath this it has to say Colon Hydrotherapy to let people know what Brightwell is My name underneath that would be Marian Holcombe And all contact details to follow this. Thanks !

Target Market(s)

People who are wanting to "detox" and focusing on their health and wellbeing

Industry/Entity Type

Clinic

Contact Information for Business Card

Brightwell
Colon Hydrotherapy
Marian Holcombe
Unit B, 42c Ferrand Lane, Whangarei

021 0487 3916
brightwellclinic@mailnest.example

Font styles to use
Serif

Colors
cee9f6
33a6d7
86cae6

Requirements
Must have
• Stand out with colour or logo

```html
<!DOCTYPE html>
<html lang="en">
<head>
<meta charset="utf-8">
<title>Brightwell Colon Hydrotherapy – Business Card</title>
<link rel="stylesheet" href="https://fonts.googleapis.com/css2?family=Cinzel:wght@400;500&family=Tinos:wght@400;700&display=swap">
<style>
  :root {
    --page-bg: #e4e7e9;
    --band-deep: #1b4f63;
    --band-mid: #2b6c82;
    --band-light: #cee9f6;
    --water-deep: #2f8fc4;
    --water-main: #33a6d7;
    --water-pale: #86cae6;
    --title-ink: #ffffff;
    --contact-ink: #111111;
    --halo: #ffffff;
  }
  * { margin: 0; padding: 0; box-sizing: border-box; }
  html, body {
    width: 1200px;
    height: 902px;
    overflow: hidden;
    background: var(--page-bg);
  }
  .canvas {
    position: relative;
    width: 1200px;
    height: 902px;
  }
  .business-card {
    position: absolute;
    left: 100px;
    top: 165px;
    width: 1000px;
    height: 571px;
    overflow: hidden;
    box-shadow: 0 10px 30px rgba(0,0,0,0.18);
  }
  .brand-band {
    position: absolute;
    left: 0; top: 0;
    width: 100%;
    height: 283px;
    background:
      radial-gradient(ellipse at 60% 30%, rgba(80,140,160,0.35), transparent 60%),
      linear-gradient(180deg, var(--band-mid) 0%, var(--band-deep) 100%);
  }
  .brand-name {
    position: absolute;
    top: 105px;
    width: 100%;
    text-align: center;
    font-family: "Cinzel", serif;
    font-weight: 400;
    font-size: 58px;
    letter-spacing: 2px;
    color: var(--title-ink);
    line-height: 1;
  }
  .brand-service {
    position: absolute;
    top: 188px;
    width: 100%;
    text-align: center;
    font-family: "Cinzel", serif;
    font-weight: 400;
    font-size: 40px;
    letter-spacing: 2px;
    color: var(--title-ink);
    line-height: 1;
  }
  .divider-band {
    position: absolute;
    left: 0; top: 283px;
    width: 100%;
    height: 44px;
    background: var(--band-light);
  }
  .water-field {
    position: absolute;
    left: 0; top: 327px;
    width: 100%;
    height: 244px;
    background: linear-gradient(180deg, var(--water-deep) 0%, var(--water-main) 45%, var(--water-pale) 100%);
  }
  .contact-block {
    position: absolute;
    left: 0; top: 327px;
    width: 100%;
    text-align: center;
    font-family: "Tinos", serif;
    color: var(--contact-ink);
    text-shadow:
      1px 1px 0 var(--halo), -1px -1px 0 var(--halo),
      1px -1px 0 var(--halo), -1px 1px 0 var(--halo),
      0 0 4px var(--halo);
  }
  .contact-name {
    position: absolute;
    top: 20px;
    width: 100%;
    font-weight: 700;
    font-size: 44px;
    line-height: 1;
  }
  .contact-line {
    position: absolute;
    width: 100%;
    font-weight: 400;
    font-size: 32px;
    line-height: 1;
  }
  .contact-phone { top: 94px; }
  .contact-email { top: 133px; }
  .contact-address { top: 174px; }
</style>
</head>
<body>
  <main class="canvas">
    <section class="business-card">
      <header class="brand-band">
        <h1 class="brand-name">Brightwell Colon</h1>
        <p class="brand-service">Hydrotherapy</p>
      </header>
      <div class="divider-band"></div>
      <div class="water-field" role="img" aria-label="Rippling blue water surface"></div>
      <address class="contact-block">
        <p class="contact-name">Marian Holcombe</p>
        <p class="contact-line contact-phone">021 0487 3916</p>
        <p class="contact-line contact-email">brightwellclinic@mailnest.example</p>
        <p class="contact-line contact-address">Unit B, 42c Ferrand Lane, Whangarei</p>
      </address>
    </section>
  </main>
</body>
</html>
```